Business card with logo for a family psychologist

I need a business card for my private practice in the urban Chicago area as a psychologist. I see families and individuals who are going through difficult times - divorce, separation, illness, or trauma. I want to project hopefulness, competence, and caring.

Target Market(s)

Adults, other professionals - such as physicans and lawyers

Industry/Entity Type

Health Care

Contact Information for Business Card

Front should have my name and credentials; back should have location information including my email, phone

Font styles to use
Serif
Decorative
Script

Requirements
Must have
• Unique logo
Should not have
• No pictures or icons of people; no black

```html
<!DOCTYPE html>
<html lang="en">
<head>
<meta charset="utf-8">
<title>Dana Whitfield, Ph.D. – Business Card</title>
<link rel="stylesheet" href="https://fonts.googleapis.com/css2?family=Open+Sans:wght@400;600&display=swap">
<style>
  :root {
    --page: #e9e4dc;
    --card: #f4f0be;
    --mauve: #b38c8c;
    --apricot: #e8a672;
    --rose-gold: #c58f7c;
    --ink: #3a2f2f;
    --white: #ffffff;
  }
  * { box-sizing: border-box; margin: 0; padding: 0; }
  html, body { width: 1200px; height: 891px; overflow: hidden; }
  body {
    background: var(--page);
    font-family: "Open Sans", sans-serif;
    display: flex;
    align-items: center;
    justify-content: center;
    gap: 40px;
  }
  .card {
    position: relative;
    width: 540px;
    height: 309px;
    background: var(--card);
    box-shadow: 0 6px 18px rgba(60, 40, 30, 0.18);
    overflow: hidden;
  }
  .band { position: absolute; left: 0; right: 0; }
  .band--mauve { background: var(--mauve); }
  .band--apricot { background: var(--apricot); }

  /* front */
  .front .brand {
    position: absolute;
    left: 0; right: 0; top: 62px;
    display: flex; align-items: center; justify-content: center; gap: 12px;
    color: var(--rose-gold);
    font-weight: 600;
    font-size: 30px;
    letter-spacing: 1px;
  }
  .brand-dot {
    width: 22px; height: 22px; border-radius: 50%;
    border: 3px solid var(--rose-gold);
  }
  .front .band--mauve { top: 196px; height: 22px; }
  .front .band--apricot { top: 218px; height: 46px; }
  .front .identity {
    position: absolute; left: 34px; top: 220px;
    color: var(--white);
  }
  .identity .name { font-size: 21px; font-weight: 600; line-height: 1.2; }
  .identity .title { font-size: 11px; letter-spacing: 0.4px; }

  /* back */
  .back .brand {
    position: absolute; left: 28px; top: 30px;
    display: flex; align-items: center; gap: 7px;
    color: var(--rose-gold); font-weight: 600; font-size: 14px;
  }
  .back .brand-dot { width: 12px; height: 12px; border-width: 2px; }
  .back .band--mauve { top: 238px; height: 20px; }
  .back .band--apricot { top: 258px; height: 14px; }
  .contact {
    position: absolute; left: 230px; top: 118px;
    color: var(--ink); font-size: 11px; line-height: 1.45;
  }
  .contact-row { display: flex; align-items: flex-start; gap: 10px; margin-bottom: 10px; }
  .contact-row svg { flex: none; margin-top: 2px; }
</style>
</head>
<body>
  <section class="card front" aria-label="Card front">
    <div class="brand"><span class="brand-dot"></span>Whitfield</div>
    <div class="band band--mauve"></div>
    <div class="band band--apricot"></div>
    <div class="identity">
      <p class="name">Dana Whitfield, Ph.D.</p>
      <p class="title">Licensed Clinical Psychologist</p>
    </div>
  </section>

  <section class="card back" aria-label="Card back">
    <div class="brand"><span class="brand-dot"></span>Whitfield</div>
    <div class="contact">
      <div class="contact-row">
        <svg width="22" height="18" viewBox="0 0 22 18" fill="none" stroke="var(--rose-gold)" stroke-width="1.4">
          <path d="M2 9 L11 2 L20 9"/><path d="M4 8 V17 H18 V8"/><rect x="9" y="11" width="4" height="6"/>
        </svg>
        <div>
          <p>240 W. Lakeview Ave Suite 310</p>
          <p>Chicago, Illinois 60614</p>
          <p>312 555-0148</p>
        </div>
      </div>
      <div class="contact-row">
        <svg width="22" height="16" viewBox="0 0 22 16" fill="none" stroke="var(--rose-gold)" stroke-width="1.4">
          <rect x="1" y="1" width="20" height="14"/><path d="M1 1 L11 9 L21 1"/>
        </svg>
        <p>drdanawhitfield@mail.com</p>
      </div>
    </div>
    <div class="band band--mauve"></div>
    <div class="band band--apricot"></div>
  </section>
</body>
</html>
```